Orbel Appraisals website redesign

I would like to refresh my existing website of www.orbelappraisals-demo.com with new graphics, look and feel, as well as updated structure and wording. Content and layout changes have been uploaded to this project Brief.

My existing website has a dark feel. I am now looking for a light and energetic feel. Financial Services is my industry, so the website should be reflect that. I would also like to reflect the concepts of Trust, Service and Expertise.

The website must be serious and upmarket.

Target Market(s)

Corporate board members, CFO's, treasurers and controllers
Auditors, tax advisors, private equity and venture capital asset managers, investors, tax authorities

Industry/Entity Type

Financial Service

Coding

Coded - Design and coding required

Number of Pages Required

5+ page

Font styles to use
Sans Serif
Other font styles liked:
• Designer can choose another modern font

Colors
0355a3
3277b5
85acd3
eaf1f7
f37122
f68d4d
9bcb3c
acd037
cadf82

Requirements
Must have
• Good hi resolution pictures that convey "Finance", "Trust", "Service" or "Expertise".
• An anti-bot (such as Captcha) mechanism in the contact form.
Should not have
• Must not have all content on one rolling screen.

```html
<!DOCTYPE html>
<html lang="en">
<head>
<meta charset="utf-8">
<title>Orbel Appraisals</title>
<link href="https://fonts.googleapis.com/css2?family=Montserrat:wght@500;600;700;800&family=Lato:ital,wght@0,400;0,700;1,400&display=swap" rel="stylesheet">
<style>
:root{
  --navy:#2f3a5c;
  --navy-dark:#1f2638;
  --orange:#ef4c12;
  --orange-soft:#fde9e1;
  --text:#3b3b3b;
  --white:#ffffff;
  --star:#f6b81c;
}
*{margin:0;padding:0;box-sizing:border-box}
html,body{width:1200px;height:3980px;overflow:hidden;background:var(--white)}
body{position:relative;font-family:'Lato',sans-serif;color:var(--text)}
.abs{position:absolute}
.heading{font-family:'Montserrat',sans-serif;font-weight:800;color:var(--navy);letter-spacing:.5px}
.btn{position:absolute;display:flex;align-items:center;justify-content:center;font-family:'Montserrat',sans-serif;font-weight:700;font-size:16px;color:var(--white);border-radius:24px 24px 0 24px}
.btn--orange{background:var(--orange)}
.btn--navy{background:var(--navy)}

/* header */
.site-header{position:absolute;left:0;top:0;width:1200px;height:112px;background:var(--white)}
.brand{position:absolute;left:112px;top:58px;width:190px;height:36px;border:2px solid #666;display:flex;align-items:center;justify-content:center;font-family:'Montserrat',sans-serif;font-weight:500;font-size:17px;color:#555}
.phone{position:absolute;left:845px;top:10px;width:240px;height:46px;background:var(--orange);border-radius:24px 24px 0 24px;display:flex;align-items:center;justify-content:center;gap:10px;color:var(--white);font-family:'Montserrat',sans-serif;font-weight:700;font-size:19px}
.main-nav a{position:absolute;top:74px;font-family:'Montserrat',sans-serif;font-weight:600;font-size:15px;color:#222;text-decoration:none}
.main-nav a.is-active{color:var(--orange)}

/* hero */
.hero-photo{position:absolute;left:0;top:112px;width:1200px;height:720px;background:linear-gradient(110deg,#4e5c70 0%,#2e3f55 40%,#4a6a8a 75%,#7d97b0 100%)}
.hero-title{left:112px;top:255px;font-size:60px;color:var(--white)}
.hero-text{left:113px;top:355px;width:620px;font-size:21px;line-height:38px;color:var(--white)}
.arrow{position:absolute;width:22px;height:22px;border-right:4px solid var(--white);border-top:4px solid var(--white)}

/* about */
.about-photo{position:absolute;left:0;top:858px;width:560px;height:475px;clip-path:polygon(0 0,420px 0,560px 475px,0 475px);background:linear-gradient(135deg,#a88670 0%,#d8d4cf 40%,#eef1f4 70%,#c8d3dc 100%)}
.about-title{left:600px;top:913px;font-size:40px}
.about-text{left:600px;top:1003px;width:490px;font-size:15px;line-height:31px;text-align:justify;color:#333}

/* services */
.services-title{left:0;width:1200px;top:1607px;text-align:center;font-size:40px;color:var(--white)}
.service-card{position:absolute;top:1750px;width:306px;height:380px}
.service-photo{position:absolute;left:0;top:0;width:306px;height:176px;background:linear-gradient(135deg,#b7b2ab,#6e6a66)}
.service-body{position:absolute;left:18px;top:128px;width:270px;height:252px;background:var(--white)}
.service-name{position:absolute;left:0;top:82px;width:270px;text-align:center;font-family:'Montserrat',sans-serif;font-weight:700;font-size:16px;color:var(--navy)}
.service-text{position:absolute;left:22px;top:118px;width:226px;font-size:14px;line-height:20px;text-align:center;color:#555}
.service-card .btn{left:136px;top:335px;width:136px;height:45px}

/* testimonials */
.testimonials-title{left:0;width:1200px;top:2310px;text-align:center;font-size:40px}
.quote-card{position:absolute;top:2418px;width:468px;height:412px;border-radius:22px;background:var(--white);box-shadow:0 4px 14px rgba(0,0,0,.12)}
.quote-card--featured{background:var(--orange-soft);box-shadow:none}
.stars{position:absolute;left:48px;top:42px;font-size:26px;letter-spacing:4px;color:var(--star)}
.quote-mark{position:absolute;left:32px;top:98px;font-family:'Montserrat',sans-serif;font-weight:800;font-size:34px;color:var(--navy)}
.quote-text{position:absolute;left:64px;top:132px;width:378px;font-style:italic;font-size:15px;line-height:26px;color:#444}
.quote-tail{position:absolute;top:412px;width:0;height:0;border-left:36px solid var(--navy);border-bottom:28px solid transparent}

/* careers */
.careers-title{left:0;width:1200px;top:3095px;text-align:center;font-size:40px}
.careers-sub{left:0;width:1200px;top:3166px;text-align:center;font-family:'Montserrat',sans-serif;font-weight:700;font-size:23px;color:var(--orange)}
.careers-text{left:220px;width:760px;text-align:center;font-size:16px;line-height:31px;color:#333}

/* footer */
.footer-nav a{position:absolute;top:3805px;font-family:'Montserrat',sans-serif;font-weight:500;font-size:15px;color:var(--white);text-decoration:none}
.footer-copy{left:0;width:1200px;top:3846px;text-align:center;font-family:'Montserrat',sans-serif;font-size:16px;color:var(--white)}
.footer-rule{left:60px;top:3882px;width:1080px;height:1px;background:var(--orange)}
.social{position:absolute;top:3914px;width:22px;height:22px;background:var(--orange);border-radius:4px}
.footer-badge{left:525px;top:3650px;width:150px;height:150px;border-radius:50%;background:var(--white);display:flex;align-items:center;justify-content:center;text-align:center;font-family:'Montserrat',sans-serif;font-weight:700;font-size:17px;line-height:22px;color:var(--orange)}
</style>
</head>
<body>

<!-- Hero image and wave -->
<div class="hero-photo" role="img" aria-label="Stacks of coins in front of a city skyline with rising financial charts"></div>
<svg class="abs" style="left:0;top:0" width="1200" height="900" viewBox="0 0 1200 900">
  <path d="M0 590 C120 700 300 770 520 755 C760 740 900 700 1050 728 C1130 742 1180 790 1200 820 L1200 900 L0 900 Z" fill="#ffffff"/>
  <path d="M0 590 C120 700 300 770 520 755 C760 740 900 700 1050 728 C1130 742 1180 790 1200 820" fill="none" stroke="var(--orange)" stroke-width="8"/>
</svg>

<header class="site-header">
  <div class="brand">Orbel Appraisals</div>
  <div class="phone">
    <svg width="18" height="18" viewBox="0 0 24 24"><path fill="#fff" d="M6.6 10.8a15 15 0 0 0 6.6 6.6l2.2-2.2c.3-.3.7-.4 1-.2 1.1.4 2.3.6 3.6.6.6 0 1 .4 1 1V20c0 .6-.4 1-1 1A17 17 0 0 1 3 4c0-.6.4-1 1-1h3.5c.6 0 1 .4 1 1 0 1.3.2 2.5.6 3.6.1.3 0 .7-.2 1z"/></svg>
    +31 70 555 0142
  </div>
  <nav class="main-nav">
    <a class="is-active" style="left:424px">HOME</a>
    <a style="left:516px">SERVICES</a>
    <a style="left:640px">NEWS &amp; VIEWS</a>
    <a style="left:794px">ABOUT</a>
    <a style="left:886px">CAREERS</a>
    <a style="left:1010px">CONTACT</a>
  </nav>
</header>

<h1 class="abs heading hero-title">ORBEL APPRAISALS</h1>
<p class="abs hero-text">Lorem ipsum dolor sit amet, consectetur adipiscing elit, sed do eiusmod tempor incididunt</p>
<a class="btn btn--orange" style="left:110px;top:470px;width:136px;height:42px;font-size:15px">READ MORE</a>
<span class="arrow" style="left:60px;top:394px;transform:rotate(-135deg)"></span>
<span class="arrow" style="left:1124px;top:394px;transform:rotate(45deg)"></span>

<!-- About -->
<svg class="abs" style="left:0;top:1320px" width="510" height="40" viewBox="0 0 510 40"><path d="M0 6 L490 12 L506 38 L0 22 Z" fill="var(--orange)"/></svg>
<div class="about-photo" role="img" aria-label="Hand with a pen reviewing financial charts on paper"></div>
<h2 class="abs heading about-title">ABOUT US</h2>
<p class="abs about-text">Orbel Appraisals, founded in 2012, is a boutique valuation advisory practice servicing companies throughout Europe and North America. We have offices in Leiden and Amsterdam. Through our affiliate partners, we also have offices in New York and London offering transfer pricing, derivatives modelling, and machinery &amp; equipment valuation. Our clients come from a broad range of industries with valuations ranging between micro-cap and large-cap.</p>
<a class="btn btn--navy" style="left:600px;top:1262px;width:137px;height:44px">READ MORE</a>

<!-- Services -->
<svg class="abs" style="left:0;top:1390px" width="1200" height="826" viewBox="0 0 1200 826">
  <rect x="0" y="0" width="1200" height="826" fill="var(--navy)"/>
  <path d="M0 0 L1200 0 L1200 280 C1120 170 1000 110 820 100 C640 90 520 140 300 135 C130 130 50 80 0 10 Z" fill="#ffffff"/>
  <path d="M0 10 C50 80 130 130 300 135 C520 140 640 90 820 100 C1000 110 1120 170 1200 280" fill="none" stroke="var(--orange)" stroke-width="8"/>
</svg>
<h2 class="abs heading services-title">SERVICES</h2>
<span class="arrow" style="left:62px;top:1910px;transform:rotate(-135deg)"></span>
<span class="arrow" style="left:1128px;top:1910px;transform:rotate(45deg)"></span>

<div class="service-card" style="left:115px">
  <div class="service-photo" role="img" aria-label="Stacks of coins on a desk beside a businessman"></div>
  <div class="service-body">
    <svg class="abs" style="left:0;top:-12px" width="270" height="40" viewBox="0 0 270 40"><path d="M0 24 C110 24 220 14 270 0 L270 12 C220 26 110 36 0 36 Z" fill="var(--orange)"/></svg>
    <div class="service-name">FINANCIAL REPORTING</div>
    <p class="service-text">Accounting procedures require post-transaction valuations concerning goodwill (PPA),</p>
  </div>
  <a class="btn btn--navy">READ MORE</a>
</div>
<div class="service-card" style="left:448px">
  <div class="service-photo" role="img" aria-label="Hands writing on documents with a pen" style="background:linear-gradient(135deg,#d8d8d8,#5a5a5a)"></div>
  <div class="service-body">
    <svg class="abs" style="left:0;top:-12px" width="270" height="40" viewBox="0 0 270 40"><path d="M0 24 C110 24 220 14 270 0 L270 12 C220 26 110 36 0 36 Z" fill="var(--orange)"/></svg>
    <div class="service-name">FISCAL VALUATIONS</div>
    <p class="service-text">Our Valuation Services assesses the value of equity investments for Dutch fiscal purposes,</p>
  </div>
  <a class="btn btn--navy">READ MORE</a>
</div>
<div class="service-card" style="left:782px">
  <div class="service-photo" role="img" aria-label="Business people in a meeting" style="background:linear-gradient(135deg,#4a4744,#a39c94)"></div>
  <div class="service-body">
    <svg class="abs" style="left:0;top:-12px" width="270" height="40" viewBox="0 0 270 40"><path d="M0 24 C110 24 220 14 270 0 L270 12 C220 26 110 36 0 36 Z" fill="var(--orange)"/></svg>
    <div class="service-name">LEGAL SUPPORT</div>
    <p class="service-text">Dutch law requires an “inbrengverklaring” (contribution in kind statement)</p>
  </div>
  <a class="btn btn--navy">READ MORE</a>
</div>

<!-- Testimonials -->
<h2 class="abs heading testimonials-title">TESTIMONIALS</h2>
<div class="quote-card quote-card--featured" style="left:122px">
  <div class="stars">★★★★☆</div>
  <div class="quote-mark">“</div>
  <p class="quote-text">Lorem ipsum dolor sit amet, consectetur adipiscing elit, sed do eiusmod tempor incididunt ut labore et dolore magna aliqua. Quis ipsum suspendisse ultrices gravida. Risus commodo viverra maecenas accumsan lacus vel facilisis. Lorem ipsum dolor sit amet, consectetur adipiscing elit, sed do eiusmod tempor incididunt ut labore et dolore magna</p>
  <span class="quote-tail" style="left:46px"></span>
</div>
<div class="quote-card" style="left:610px">
  <div class="stars">★★★★☆</div>
  <div class="quote-mark">“</div>
  <p class="quote-text">Lorem ipsum dolor sit amet, consectetur adipiscing elit, sed do eiusmod tempor incididunt ut labore et dolore magna aliqua. Quis ipsum suspendisse ultrices gravida. Risus commodo viverra maecenas accumsan lacus vel facilisis. Lorem ipsum dolor sit amet, consectetur adipiscing elit, sed do eiusmod tempor incididunt ut labore et dolore magna</p>
  <span class="quote-tail" style="left:46px"></span>
</div>

<!-- Careers -->
<h2 class="abs heading careers-title">CAREERS</h2>
<div class="abs careers-sub">JOB OPENINGS</div>
<p class="abs careers-text" style="top:3238px">Orbel Appraisals is a growing firm with a thin hierarchical structure. We offer you on-the-job training and involvement in the decision making processes.</p>
<p class="abs careers-text" style="top:3330px">Choose from one of the positions listed on the left or send an open solicitation to careers@orbelappraisals-demo.com. We look forward to hearing from you.</p>
<a class="btn btn--navy" style="left:532px;top:3448px;width:137px;height:44px">READ MORE</a>

<!-- Footer -->
<svg class="abs" style="left:0;top:3560px" width="1200" height="420" viewBox="0 0 1200 420">
  <path d="M0 300 C120 200 300 110 520 120 C680 128 800 140 960 110 C1080 88 1160 50 1200 0 L1200 420 L0 420 Z" fill="var(--navy-dark)"/>
</svg>
<div class="abs footer-badge">Orbel<br>Appraisals</div>
<nav class="footer-nav">
  <a style="left:293px">HOME</a>
  <a style="left:370px">SERVICES</a>
  <a style="left:485px">NEWS &amp; VIEWS</a>
  <a style="left:640px">ABOUT</a>
  <a style="left:716px">CAREERS</a>
  <a style="left:832px">CONTACT</a>
</nav>
<p class="abs footer-copy">© 2019 WWW.ORBELAPPRAISALS-DEMO.COM RIGHTS RESERVED</p>
<div class="abs footer-rule"></div>
<span class="social" style="left:503px"></span>
<span class="social" style="left:558px"></span>
<span class="social" style="left:612px"></span>
<span class="social" style="left:666px"></span>

</body>
</html>
```